Prairie Kettle Billboard

We are looking to have a new billboard design for our Casual Restaurant chain. We are a steakhouse chain that is very casual. You can visit our website at: www.prairiekettle-demo.net to get an idea of our menu. We are looking to have some new billboard ideas for our steakhouse so that we can communicate our concept to customers that are passing by the billboard. I have attached some items to give you a feel for our concept. The Billboard will be 14'X48'. I look forward to hearing from you. Glen

```html
<!DOCTYPE html>
<html lang="en">
<head>
<meta charset="utf-8">
<title>Prairie Kettle Billboard</title>
<link href="https://fonts.googleapis.com/css2?family=Roboto+Condensed:wght@900&family=Arimo:wght@700&display=swap" rel="stylesheet">
<style>
  :root {
    --board-black: #000000;
    --page-white: #ffffff;
    --headline-white: #ffffff;
    --accent-yellow: #ffec00;
    --brand-red: #c8231b;
    --ember-orange: #e2560f;
    --steak-brown: #5a2e1a;
  }
  html, body {
    margin: 0;
    padding: 0;
    width: 1200px;
    height: 392px;
    overflow: hidden;
    background: var(--page-white);
  }
  .billboard {
    position: relative;
    width: 1200px;
    height: 328px;
    background: var(--board-black);
    overflow: hidden;
  }
  .grill-photo {
    position: absolute;
    left: 300px;
    top: 0;
    width: 680px;
    height: 328px;
    background:
      radial-gradient(ellipse 46% 40% at 52% 50%, #8a4a2c 0%, var(--steak-brown) 45%, rgba(40,15,8,0.9) 75%, transparent 100%),
      radial-gradient(ellipse 60% 35% at 50% 100%, #ff6a10 0%, #a52a06 45%, transparent 80%),
      radial-gradient(ellipse 55% 30% at 50% 0%, var(--ember-orange) 0%, #7a1c05 50%, transparent 85%),
      linear-gradient(90deg, var(--board-black) 0%, #2a0a03 18%, #2a0a03 82%, var(--board-black) 100%);
  }
  .headline {
    position: absolute;
    left: 22px;
    margin: 0;
    font-family: "Roboto Condensed", "Arial Narrow", sans-serif;
    font-weight: 900;
    color: var(--headline-white);
    line-height: 1;
    transform-origin: left top;
  }
  .headline-i {
    top: -14px;
    font-size: 190px;
    transform: scaleX(0.9);
  }
  .headline-steak {
    top: 146px;
    font-size: 196px;
    letter-spacing: -4px;
    transform: scaleX(0.86);
  }
  .heart {
    position: absolute;
    left: 78px;
    top: 8px;
    width: 246px;
    height: 146px;
  }
  .brand {
    position: absolute;
    left: 982px;
    top: 62px;
    width: 190px;
    display: flex;
    align-items: center;
    justify-content: center;
    gap: 8px;
  }
  .brand-dot {
    width: 16px;
    height: 16px;
    border-radius: 50%;
    background: var(--brand-red);
    flex: none;
  }
  .brand-name {
    font-family: "Arimo", Arial, sans-serif;
    font-weight: 700;
    font-size: 22px;
    color: var(--brand-red);
    white-space: nowrap;
  }
  .address {
    position: absolute;
    left: 972px;
    top: 152px;
    width: 200px;
    margin: 0;
    text-align: center;
    font-family: "Arimo", Arial, sans-serif;
    font-weight: 700;
    font-size: 17px;
    line-height: 1.3;
    color: var(--headline-white);
  }
  .phone {
    position: absolute;
    left: 730px;
    top: 234px;
    display: flex;
    align-items: center;
    font-family: "Arimo", Arial, sans-serif;
    font-weight: 700;
    color: var(--accent-yellow);
  }
  .phone-area {
    font-size: 26px;
    transform: rotate(-90deg);
    width: 30px;
    margin-right: 6px;
    text-align: center;
  }
  .phone-number {
    font-size: 82px;
    line-height: 1;
    letter-spacing: -1px;
  }
</style>
</head>
<body>
  <main class="billboard">
    <div class="grill-photo" role="img" aria-label="Seared steak on a grill over open flames"></div>

    <p class="headline headline-i">I</p>
    <svg class="heart" viewBox="0 0 246 146" aria-label="love">
      <path d="M123 146 C70 118 8 88 8 42 C8 16 30 2 58 2 C88 2 110 18 123 38 C136 18 158 2 188 2 C216 2 238 16 238 42 C238 88 176 118 123 146 Z" fill="var(--accent-yellow)"/>
    </svg>
    <p class="headline headline-steak">STEAK</p>

    <div class="brand">
      <span class="brand-dot"></span>
      <span class="brand-name">Prairie Kettle</span>
    </div>

    <p class="address">4100 Meridian<br>Boulevard</p>

    <div class="phone">
      <span class="phone-area">219</span>
      <span class="phone-number">555-0147</span>
    </div>
  </main>
</body>
</html>
```